Stationary for IT communtications company
We send SMS and email messages to pet owners from veterinary practices
Stationary for IT communtications company - Information Technology
Creative Brief
Modern
Dominic Pelling MRCVS
Mr
Oakmere Stanhurst Lode Norwich NR14 2QJ
dominic@quietnudge.co.uk
www.quietnudge.co.uk
Quiet Nudge Logo

```html
<!DOCTYPE html>
<html lang="en">
<head>
<meta charset="utf-8">
<title>Quiet Nudge – Business Cards</title>
<link rel="stylesheet" href="https://fonts.googleapis.com/css2?family=Roboto:wght@400;700;900&display=swap">
<style>
  :root {
    --bg: #e9e9e6;
    --card: #ffffff;
    --green: #5f9a1f;
    --green-dark: #3f7410;
    --green-light: #8cc43c;
    --green-glow: #c4dc4a;
    --ink: #1d1d1d;
    --swoosh: #111111;
    --white: #ffffff;
  }
  html, body {
    margin: 0;
    width: 1200px;
    height: 901px;
    overflow: hidden;
    background: var(--bg);
    font-family: "Roboto", Arial, sans-serif;
  }
  .card {
    position: absolute;
    width: 680px;
    height: 422px;
    border-radius: 16px;
    overflow: hidden;
    box-shadow: 0 8px 24px rgba(0,0,0,.18);
  }

  /* Back side */
  .card-back {
    left: 60px;
    top: 28px;
    background: radial-gradient(ellipse at 28% 32%, var(--green-glow) 0%, var(--green-light) 30%, var(--green) 65%, var(--green-dark) 100%);
  }
  .card-back .brand {
    position: absolute;
    left: 60px;
    top: 170px;
    display: flex;
    align-items: center;
    gap: 18px;
  }
  .card-back .brand-dot {
    width: 66px;
    height: 66px;
    border-radius: 50%;
    background: var(--white);
  }
  .card-back .brand-name {
    font-weight: 900;
    font-size: 58px;
    color: var(--white);
    text-transform: uppercase;
    line-height: 1;
    letter-spacing: 1px;
  }
  .card-back .back-web {
    position: absolute;
    right: 40px;
    top: 252px;
    margin: 0;
    font-size: 13px;
    color: var(--white);
  }

  /* Front side */
  .card-front {
    left: 460px;
    top: 462px;
    background: var(--card);
  }
  .card-art {
    position: absolute;
    inset: 0;
  }
  .card-front .brand {
    position: absolute;
    right: 38px;
    top: 46px;
    display: flex;
    align-items: center;
    gap: 14px;
  }
  .card-front .brand-dot {
    width: 50px;
    height: 50px;
    border-radius: 50%;
    background: var(--green);
  }
  .card-front .brand-name {
    font-weight: 900;
    font-size: 50px;
    letter-spacing: 1px;
    color: var(--ink);
    text-transform: uppercase;
    line-height: 1;
  }
  .holder {
    position: absolute;
    left: 330px;
    width: 290px;
    top: 205px;
    text-align: center;
    color: var(--ink);
  }
  .holder-name {
    font-weight: 700;
    font-size: 20px;
    margin: 0;
  }
  .holder-title {
    font-size: 16px;
    margin: 4px 0 0;
  }
  .contact {
    position: absolute;
    left: 28px;
    color: var(--white);
    font-size: 13px;
    line-height: 1.3;
    margin: 0;
  }
  .contact.address { top: 218px; }
  .contact.lines { top: 272px; }
  .contact.web { top: 386px; }
</style>
</head>
<body>
  <div class="card card-back">
    <div class="brand">
      <span class="brand-dot"></span>
      <span class="brand-name">Quiet Nudge</span>
    </div>
    <p class="back-web">www.quietnudge.co.uk</p>
  </div>

  <div class="card card-front">
    <svg class="card-art" viewBox="0 0 1000 620" width="680" height="422" preserveAspectRatio="none" aria-hidden="true">
      <defs>
        <linearGradient id="greenFill" x1="0" y1="0" x2="1" y2="1">
          <stop offset="0" stop-color="#8cc43c"/>
          <stop offset="0.45" stop-color="#5f9a1f"/>
          <stop offset="1" stop-color="#3f7410"/>
        </linearGradient>
      </defs>
      <path d="M0,255 C240,250 420,420 660,500 C800,545 920,545 1000,520 L1000,620 L0,620 Z" fill="url(#greenFill)"/>
      <path d="M0,238 C250,232 430,400 670,478 C810,522 930,520 1000,498" fill="none" stroke="#111111" stroke-width="7"/>
      <path d="M120,236 C300,250 450,390 690,466 C820,506 930,498 1000,476" fill="none" stroke="#111111" stroke-width="3"/>
    </svg>

    <div class="brand">
      <span class="brand-dot"></span>
      <span class="brand-name">Quiet Nudge</span>
    </div>

    <div class="holder">
      <p class="holder-name">Dominic Pelling MRCVS</p>
      <p class="holder-title">Mr</p>
    </div>

    <p class="contact address">Oakmere, Stanhurst, Lode<br>Norwich, NR14 2QJ</p>
    <p class="contact lines">C: 07700 900418<br>E: dominic@quietnudge.co.uk</p>
    <p class="contact web">www.quietnudge.co.uk</p>
  </div>
</body>
</html>
```